Fancy looking Inspection Postcard

Postcard needed for customers to inspect their product once it is delivered. We'll be giving them the steps for inspecting their product and to contact us if any issues arise. Would like to see something that sticks out but uses our company's colors. Would like to see creativity. Possibly utilizing the diamond steel background like we have in our logo.

Target Market(s)

Customers of our manufacturing shop

Industry/Entity Type

Manufacturing - metal wall art, custom products

Requirements
Must have
• our colors and logo
Nice to have
• get creative. i like creativity

```html
<!DOCTYPE html>
<html lang="en">
<head>
<meta charset="utf-8">
<title>Ridgeline Fabrication – Inspection Postcard</title>
<link rel="stylesheet" href="https://fonts.googleapis.com/css2?family=Oswald:wght@500;600&family=Roboto:wght@400;500&display=swap">
<style>
  :root{
    --bg:#d9dadc;
    --ink:#0d0e0f;
    --plate-dark:#121314;
    --plate-mid:#2a2c2e;
    --panel:#1d1e20;
    --yellow:#f5e21b;
    --yellow-deep:#e9c911;
    --green:#7cb342;
    --silver:#b9bcc0;
    --white:#ffffff;
    --line:#b8b8b8;
  }
  *{box-sizing:border-box;margin:0;padding:0}
  html,body{width:1200px;height:930px;overflow:hidden}
  body{background:var(--bg);font-family:"Roboto",Arial,sans-serif;position:relative}

  .card{position:absolute;width:620px;height:413px;overflow:hidden;box-shadow:0 10px 26px rgba(0,0,0,.28);background:var(--plate-dark)}
  .card--front{left:30px;top:30px}
  .card--back{left:550px;top:487px;background:var(--white)}

  .plate{position:absolute;inset:0;background:radial-gradient(ellipse at 30% 20%,var(--plate-mid),var(--plate-dark) 70%)}
  .front-panel{position:absolute;inset:0;background:linear-gradient(160deg,#2b2d30,var(--panel) 60%);clip-path:polygon(72% 0,100% 0,100% 100%,64% 100%)}

  .steps{position:absolute;left:0;top:26px;width:400px}
  .step{margin-bottom:12px}
  .step__head{display:flex;align-items:stretch;height:24px}
  .step__num{background:var(--green);color:var(--ink);font:600 17px/24px "Oswald",sans-serif;padding:0 10px 0 18px}
  .step__title{background:var(--yellow);color:var(--ink);font:600 17px/24px "Oswald",sans-serif;padding:0 26px 0 10px;clip-path:polygon(0 0,100% 0,92% 100%,0 100%)}
  .step__list{list-style:none;padding:4px 0 0 30px}
  .step__list li{color:var(--white);font-size:14px;line-height:19px;display:flex;align-items:center;gap:9px}
  .step__list li::before{content:"";width:11px;height:11px;background:var(--yellow);flex:none}

  .wordmark{position:absolute;display:flex;flex-direction:column;align-items:center;text-align:center;color:var(--green);font-family:"Oswald",sans-serif;font-weight:600;line-height:1}
  .wordmark__dot{width:46px;height:46px;border-radius:50%;background:var(--yellow);margin-bottom:12px}
  .wordmark--front{left:400px;top:70px;width:220px;font-size:38px}
  .wordmark--front small{font-size:24px;letter-spacing:3px;margin-top:6px}
  .wordmark--back{left:95px;top:22px;width:180px;font-size:30px}
  .wordmark--back small{font-size:19px;letter-spacing:2px;margin-top:4px}
  .wordmark--back .wordmark__dot{width:36px;height:36px;margin-bottom:10px}

  .silver-rule{position:absolute;left:0;right:0;height:5px;background:linear-gradient(90deg,#777,var(--silver),#888)}
  .contact-band{position:absolute;left:0;right:0;bottom:0;height:56px;background:linear-gradient(180deg,var(--yellow),var(--yellow-deep));display:flex;align-items:center;justify-content:space-between;padding:0 22px;color:var(--ink);font:500 16px "Roboto",sans-serif}
  .contact{display:flex;align-items:center;gap:7px}
  .contact svg{width:16px;height:16px;flex:none}

  .back-dark{position:absolute;inset:0;clip-path:polygon(0 0,57% 0,69% 100%,0 100%)}
  .review{position:absolute;left:10px;top:178px;width:360px;text-align:center}
  .review__brand{font:500 18px/21px "Roboto",sans-serif;color:var(--white)}
  .review__stars{color:var(--yellow);font-size:10px;line-height:14px;letter-spacing:2px;margin-bottom:6px}
  .review__ask{font:500 15px/19px "Oswald",sans-serif;color:var(--green);white-space:nowrap}
  .review__note{font-size:12.5px;line-height:17px;color:var(--white);margin-top:6px}
  .back-band-green{position:absolute;left:0;bottom:56px;height:26px;width:215px;background:var(--green);clip-path:polygon(0 0,100% 0,90% 100%,0 100%);display:flex;align-items:center;padding-left:14px;gap:6px;color:var(--white);font-size:12.5px}
  .back-band-green svg{width:13px;height:13px}
  .back-yellow{position:absolute;left:0;bottom:0;height:56px;width:69%;background:linear-gradient(180deg,var(--yellow),var(--yellow-deep));clip-path:polygon(0 0,96% 0,100% 100%,0 100%);display:flex;align-items:center;justify-content:space-between;padding:0 28px 0 14px;font-size:13.5px;color:var(--ink)}
  .back-yellow .contact svg{width:13px;height:13px}

  .stamp-box{position:absolute;right:30px;top:28px;width:78px;height:86px;border:2px solid #c8c8c8}
  .address-lines{position:absolute;left:445px;right:30px;top:180px}
  .address-lines span{display:block;border-bottom:1.5px solid var(--line);height:36px}
</style>
</head>
<body>

<section class="card card--front" aria-label="Postcard front: inspection steps">
  <div class="plate" role="img" aria-label="Black diamond steel plate texture"></div>
  <div class="front-panel"></div>

  <div class="steps">
    <div class="step">
      <div class="step__head"><span class="step__num">STEP 1.</span><span class="step__title">INSPECT GENERAL SHAPE</span></div>
      <ul class="step__list"><li>Is it what you expected?</li><li>Is it bent, disoriented?</li></ul>
    </div>
    <div class="step">
      <div class="step__head"><span class="step__num">STEP 2.</span><span class="step__title">INSPECT THE WELDS</span></div>
      <ul class="step__list"><li>Do they look clean?</li><li>Are there any gaps?</li></ul>
    </div>
    <div class="step">
      <div class="step__head"><span class="step__num">STEP 3.</span><span class="step__title">INSPECT THE FINISH</span></div>
      <ul class="step__list"><li>Are there any areas not finished?</li><li>Are the colors what you expected?</li></ul>
    </div>
    <div class="step">
      <div class="step__head"><span class="step__num">STEP 4.</span><span class="step__title">CHECK FOR FUNCTIONALITY</span></div>
      <ul class="step__list"><li>Does it work the way you want it to?</li><li>Is it what you expected?</li></ul>
    </div>
  </div>

  <div class="wordmark wordmark--front">
    <span class="wordmark__dot"></span>
    RIDGELINE
    <small>FABRICATION</small>
  </div>

  <div class="silver-rule" style="bottom:56px"></div>
  <div class="contact-band">
    <span class="contact">
      <svg viewBox="0 0 16 16"><circle cx="8" cy="8" r="7.2" fill="none" stroke="#0d0e0f" stroke-width="1.4"/><rect x="4" y="5.5" width="8" height="5.5" fill="none" stroke="#0d0e0f" stroke-width="1.1"/><path d="M4 5.7 8 8.6 12 5.7" fill="none" stroke="#0d0e0f" stroke-width="1.1"/></svg>
      orders@ridgelinefab.com
    </span>
    <span class="contact">
      <svg viewBox="0 0 16 16"><circle cx="8" cy="8" r="7.2" fill="none" stroke="#0d0e0f" stroke-width="1.4"/><path d="M5.3 4.4c.5-.4 1-.3 1.3.2l.7 1.3c.2.4.1.8-.2 1l-.5.4c.4.9 1.1 1.6 2 2l.4-.5c.3-.3.7-.4 1-.2l1.3.7c.5.3.6.8.2 1.3-.8 1-2 1.1-3.3.3-1.3-.8-2.5-2-3.2-3.3-.8-1.4-.6-2.5.3-3.2z" fill="#0d0e0f"/></svg>
      (555) 013-2290
    </span>
    <span class="contact">
      <svg viewBox="0 0 16 16" fill="none" stroke="#0d0e0f" stroke-width="1.2"><circle cx="8" cy="8" r="7"/><ellipse cx="8" cy="8" rx="3" ry="7"/><path d="M1 8h14M2.5 4.5h11M2.5 11.5h11"/></svg>
      www.ridgelinefab.com
    </span>
  </div>
</section>

<section class="card card--back" aria-label="Postcard back: review request and address side">
  <div class="back-dark">
    <div class="plate" role="img" aria-label="Black diamond steel plate texture"></div>
  </div>

  <div class="wordmark wordmark--back">
    <span class="wordmark__dot"></span>
    RIDGELINE
    <small>FABRICATION</small>
  </div>

  <div class="review">
    <div class="review__brand">Starlist</div>
    <div class="review__stars">★★★★★</div>
    <div class="review__ask">DID WE DO A GOOD JOB?<br>IF YOU THINK SO, LEAVE US A REVIEW ON STARLIST?</div>
    <p class="review__note">If not, Please let us know<br>info@ridgelinefab.com or call us 555-014-7731</p>
  </div>

  <div class="back-band-green">
    <svg viewBox="0 0 16 16"><circle cx="8" cy="8" r="7.2" fill="none" stroke="#fff" stroke-width="1.4"/><path d="M5.3 4.4c.5-.4 1-.3 1.3.2l.7 1.3c.2.4.1.8-.2 1l-.5.4c.4.9 1.1 1.6 2 2l.4-.5c.3-.3.7-.4 1-.2l1.3.7c.5.3.6.8.2 1.3-.8 1-2 1.1-3.3.3-1.3-.8-2.5-2-3.2-3.3-.8-1.4-.6-2.5.3-3.2z" fill="#fff"/></svg>
    (555) 013-2290
  </div>
  <div class="back-yellow">
    <span class="contact">
      <svg viewBox="0 0 16 16"><circle cx="8" cy="8" r="7.2" fill="none" stroke="#0d0e0f" stroke-width="1.4"/><rect x="4" y="5.5" width="8" height="5.5" fill="none" stroke="#0d0e0f" stroke-width="1.1"/><path d="M4 5.7 8 8.6 12 5.7" fill="none" stroke="#0d0e0f" stroke-width="1.1"/></svg>
      orders@ridgelinefab.com
    </span>
    <span class="contact">
      <svg viewBox="0 0 16 16" fill="none" stroke="#0d0e0f" stroke-width="1.2"><circle cx="8" cy="8" r="7"/><ellipse cx="8" cy="8" rx="3" ry="7"/><path d="M1 8h14M2.5 4.5h11M2.5 11.5h11"/></svg>
      www.ridgelinefab.com
    </span>
  </div>

  <div class="stamp-box" aria-hidden="true"></div>
  <div class="address-lines" aria-hidden="true"><span></span><span></span><span></span><span></span></div>
</section>

</body>
</html>
```